依頼詳細
<デザインイメージ>
・ラグジュアリー/高級なイメージ
・VIPのように扱われている
・希少な会に招待されている
記載項目
最低限記載項目:キャッチコピーや見出し/講演タイトル/日時/場所
※講演タイトル/日時/場所については、添付ファイルに記載しています。
※これを使って下さいという素材は特に決まっていません。
サイズ
A4
ページ数
片面
希望イメージ
• +5 0 +5
• シンプル
複雑
• 単色
カラフル
• 暗い
明るい
• 日常
高級
• 遊び心
厳粛
• 未来的
伝統的
• 女性的
男性的
希望する色
黄・オレンジ系、グレー系
納品ファイル
• 高解像度JPG (.jpg)
• イラストレーター形式 (.ai)
• フォトショップ形式 (.psd)
• PNG形式 (.png)
補足説明
依頼公開後の追記内容
<追記>

・講演の内容/テーマ
・講演のスケジュール
・会場について
・チケットの料金
・お申し込み方法
・お問い合わせ先

こちらについては
裏面に記載しております。

チラシ作品として非常に完成度が高かった事に加えて、内容も洗練されていたことが決め手となりました。

この度は、誠に多くのミルダー様にご提案をいただきましたことを、心から感謝いたします。皆様のご提案のクオリティがどれも高く選定にとても悩みました。

この度選定できなかったミルダー様にも、ご縁次第で、また直接ご依頼をさせていただきたいと思っておりますので、今後ともどうぞよろしくお願いいたします。

```html
<!DOCTYPE html>
<html lang="ja">
<head>
<meta charset="UTF-8">
<title>ビリオネアの授業 2018</title>
<link rel="stylesheet" href="https://fonts.googleapis.com/css2?family=Shippori+Mincho:wght@400;600;700&family=Playfair+Display:ital,wght@0,400;1,400&display=swap">
<style>
  :root {
    --ink-white: #ffffff;
    --gold: #c9a25a;
    --gold-light: #e0c183;
    --sky-top: #3e3e3e;
    --sky-mid: #8a8a8a;
    --sky-light: #b4b4b4;
    --rock-dark: #343434;
    --offer-cream: #f4ead2;
    --offer-text: #6b5320;
  }
  * { margin: 0; padding: 0; box-sizing: border-box; }
  html, body { width: 849px; height: 1200px; overflow: hidden; background: #fff; }
  .flyer {
    position: relative;
    width: 849px;
    height: 1200px;
    overflow: hidden;
    font-family: "Shippori Mincho", "Noto Serif JP", serif;
    color: var(--ink-white);
  }
  .backdrop-photo {
    position: absolute; inset: 0;
    background:
      linear-gradient(90deg, rgba(0,0,0,0) 0%, rgba(0,0,0,0) 55%, rgba(30,30,30,0.25) 100%),
      linear-gradient(180deg, var(--sky-top) 0%, #5a5a5a 16%, var(--sky-mid) 32%, var(--sky-light) 52%, #9c9c9c 66%, #5c5c5c 78%, var(--rock-dark) 90%, #262626 100%);
  }
  .lead-copy {
    position: absolute; top: 22px; left: 0; width: 100%;
    text-align: center; font-size: 38px; font-weight: 600; letter-spacing: 1px;
  }
  .headline {
    position: absolute; top: 180px; left: 0; width: 100%;
    text-align: center; font-size: 56px; font-weight: 700; line-height: 1.35;
    color: var(--gold-light);
  }
  .title-frame { position: absolute; left: 340px; top: 386px; width: 180px; height: 490px; }
  .title-frame svg { position: absolute; inset: 0; }
  .visit-label {
    position: absolute; left: 0; top: -2px; width: 100%;
    text-align: center; font-size: 17px; letter-spacing: 2px;
  }
  .lecture-title {
    position: absolute; left: 62px; top: 68px;
    writing-mode: vertical-rl; font-size: 40px; font-weight: 400; letter-spacing: 4px; line-height: 1;
  }
  .lecture-year {
    position: absolute; left: 80px; top: 408px;
    font-family: "Playfair Display", serif; font-style: italic; font-size: 34px;
  }
  .special-label {
    position: absolute; top: 975px; left: 0; width: 849px; text-align: center;
    font-family: "Playfair Display", serif; font-style: italic; font-size: 26px; color: var(--gold-light);
  }
  .lecture-theme {
    position: absolute; top: 1012px; left: 0; width: 849px; text-align: center; font-size: 17px;
  }
  .event-date {
    position: absolute; top: 1050px; left: 0; width: 849px; text-align: center;
    font-size: 30px; font-weight: 600; letter-spacing: 2px;
  }
  .event-date small { font-size: 18px; }
  .event-time {
    position: absolute; top: 1094px; left: 0; width: 849px; text-align: center; font-size: 20px;
  }
  .venue {
    position: absolute; top: 1134px; left: 0; width: 849px; text-align: center; font-size: 24px; font-weight: 600;
  }
  .venue small { font-size: 12px; font-weight: 400; margin-left: 10px; }
  .offer-badge {
    position: absolute; left: 22px; top: 1010px; width: 156px; height: 156px; border-radius: 50%;
    background: var(--offer-cream); border: 4px solid var(--gold);
    display: flex; align-items: center; justify-content: center; text-align: center;
    font-family: "Playfair Display", serif; font-size: 25px; line-height: 1.2; color: var(--offer-text);
  }
</style>
</head>
<body>
<div class="flyer">
  <div class="backdrop-photo" role="img" aria-label="雪山の稜線を見下ろす登山者の後ろ姿を写したモノクロ写真"></div>

  <p class="lead-copy">そろそろ、新しい山に挑んでみませんか。</p>
  <h1 class="headline">海外ビリオネアの実践力を<br>あなたさまに</h1>

  <div class="title-frame">
    <svg width="180" height="490" viewBox="0 0 180 490" aria-hidden="true">
      <polyline points="38,10 0,10 0,490" fill="none" stroke="#fff" stroke-width="1.2"/>
      <polyline points="142,10 180,10 180,66" fill="none" stroke="#fff" stroke-width="1.2"/>
      <line x1="30" y1="60" x2="30" y2="300" stroke="#fff" stroke-width="0.8"/>
    </svg>
    <p class="visit-label">来日講演</p>
    <h2 class="lecture-title">ビリオネアの授業</h2>
    <p class="lecture-year">2018</p>
  </div>

  <p class="special-label">Special Lecture</p>
  <p class="lecture-theme">成功、リーダーシップ、桁違いの億万長者になるには</p>
  <p class="event-date">2018年9月17日<small>(月・祝)</small></p>
  <p class="event-time">13:00～19:30 ／ 開場 12:00</p>
  <p class="venue">北浜セントラルホール<small>大阪府大阪市北区 会場案内 裏面参照</small></p>

  <div class="offer-badge">LIMITED<br>OFFER</div>
</div>
</body>
</html>
```